Business Card for TVK, logo files already created

Please, can you assist with creating a Business card the TVK graphics which are already listed on www.brinmoretech.example
The business card should be modern and upmarket, textured designs are welcome. Please feel free to express yourself and be very bold with your design.

Target Market(s)

Cyber Security

Industry/Entity Type

Information Technology

Contact Information for Business Card

Company Name
Name
Title
Mobile
Fax or Tel
email
url

Font styles to use
Serif
Sans Serif

Colors
3277b5
85acd3
ffffff

```html
<!DOCTYPE html>
<html lang="en">
<head>
<meta charset="utf-8">
<title>TVK Business Card</title>
<link href="https://fonts.googleapis.com/css2?family=Exo+2:wght@400;600;700&display=swap" rel="stylesheet">
<style>
  :root {
    --brand-blue: #0b35a0;
    --brand-gray: #55585e;
    --paper: #ffffff;
    --backdrop: #e6e7ea;
    --ink-light: #ffffff;
  }
  * { box-sizing: border-box; margin: 0; padding: 0; }
  html, body { width: 1200px; height: 900px; overflow: hidden; }
  body {
    background: var(--backdrop);
    font-family: "Exo 2", Arial, sans-serif;
    position: relative;
  }
  .card {
    position: absolute;
    left: 250px;
    width: 700px;
    height: 400px;
    background: var(--paper);
    box-shadow: 0 8px 24px rgba(0,0,0,0.18);
    overflow: hidden;
  }
  .card-front { top: 30px; }
  .card-back { top: 470px; }

  /* brand lockup */
  .brand {
    display: flex;
    align-items: center;
    gap: 14px;
    color: var(--brand-blue);
    font-weight: 700;
  }
  .brand-square {
    width: 26px; height: 26px;
    background: var(--brand-blue);
  }
  .brand-name { letter-spacing: 6px; line-height: 1; }

  /* front */
  .front-logo {
    position: absolute;
    top: 0; left: 0; right: 0; height: 250px;
    display: flex; align-items: center; justify-content: center;
  }
  .front-logo .brand-name { font-size: 110px; }
  .front-band {
    position: absolute;
    left: 0; right: 0; bottom: 0; height: 130px;
    background: var(--brand-blue);
    display: flex; align-items: center; justify-content: center;
  }
  .front-rules {
    position: absolute; left: 0; right: 0; bottom: 130px; height: 16px;
    border-top: 3px solid var(--brand-blue);
    border-bottom: 3px solid var(--brand-blue);
  }
  .front-rules::after {
    content: ""; position: absolute; left: 0; right: 0; top: 4px;
    border-top: 2px solid var(--brand-blue);
  }
  .website {
    color: var(--ink-light);
    font-size: 17px;
    font-weight: 600;
    letter-spacing: 4px;
  }

  /* back */
  .back-logo {
    position: absolute; left: 0; top: 0; bottom: 0; width: 330px;
    display: flex; align-items: center; justify-content: center;
  }
  .back-logo .brand-name { font-size: 72px; letter-spacing: 4px; }
  .back-logo .brand-square { width: 18px; height: 18px; }
  .back-rules {
    position: absolute; top: 0; bottom: 0; left: 330px; width: 18px;
    border-left: 3px solid var(--brand-blue);
    border-right: 3px solid var(--brand-blue);
  }
  .back-rules::after {
    content: ""; position: absolute; top: 0; bottom: 0; left: 4px;
    border-left: 2px solid var(--brand-blue);
  }
  .contact-panel {
    position: absolute; top: 0; bottom: 0; left: 348px; right: 0;
    background: var(--brand-blue);
    color: var(--ink-light);
    padding: 110px 0 0 50px;
  }
  .person-name { font-size: 26px; font-weight: 700; }
  .person-title { font-size: 13px; font-weight: 400; margin-top: 2px; }
  .address { font-size: 15px; font-weight: 700; margin-top: 18px; }
  .contact-list { list-style: none; margin-top: 12px; }
  .contact-item {
    display: flex; align-items: center; gap: 12px;
    font-size: 15px; margin-top: 8px;
  }
  .contact-item svg { width: 16px; height: 16px; fill: var(--ink-light); flex: none; }
  .contact-item.email { font-size: 13px; }
</style>
</head>
<body>
  <section class="card card-front">
    <div class="front-logo">
      <div class="brand"><span class="brand-square"></span><span class="brand-name">TVK</span></div>
    </div>
    <div class="front-rules"></div>
    <div class="front-band">
      <span class="website">www.brinmoretech.example</span>
    </div>
  </section>

  <section class="card card-back">
    <div class="back-logo">
      <div class="brand"><span class="brand-square"></span><span class="brand-name">TVK</span></div>
    </div>
    <div class="back-rules"></div>
    <div class="contact-panel">
      <p class="person-name">Dana Whitfield</p>
      <p class="person-title">Chief Executive Offer</p>
      <p class="address">410 Harbor Park Way, Suite 12, NC 27000</p>
      <ul class="contact-list">
        <li class="contact-item">
          <svg viewBox="0 0 16 16" aria-hidden="true"><path d="M1 5c0-2 3-3 7-3s7 1 7 3v1h-4V5H5v1H1z M3 8h10l1 6H2z"/></svg>
          <span>555.010.4821</span>
        </li>
        <li class="contact-item">
          <svg viewBox="0 0 16 16" aria-hidden="true"><path d="M4 1h8v4H4z M1 6h14v6h-3v3H4v-3H1z M5 10v3h6v-3z"/></svg>
          <span>555.010.7390</span>
        </li>
        <li class="contact-item email">
          <svg viewBox="0 0 16 16" aria-hidden="true"><path d="M1 3h14v10H1z M2 4l6 5 6-5" stroke="#0b35a0" stroke-width="1"/></svg>
          <span>contact@brinmoretech.example</span>
        </li>
      </ul>
    </div>
  </section>
</body>
</html>
```